Simple and clean poster/flyer design needed for public speaker!

SIMPLE AND CLEAN DESIGN NEEDED FOR POSTER/FLYER

I AM a public speaker based in London (www.tobiaskernwald.com)
and I would like to have a custom-made flyer/poster
(preferably in adobe CS4 template format) that I con customize (just changing the text) for my various speeches, topics and locations

I am looking for something very simple and clean.
NO extravagance or crowded poster, but a rather beautiful clean and eye-catching design that clearly informs people what i am talking about, where and when.

Go to my website www.tobiaskernwald.com
to see the colour scheme and style that I like
my poster should be like the website, similar colours, logo, clean, simple and clear.

Summary

(1) simple and clean design
(2) design that fits my brand (see website)
(3) clear and eye-catching to promote my speeches
(4) customizable for my various talks, by simply chancing the text (Please Adobe Photoshop CS4 template format)
(5)in A3, A4, A5, A6 sizes, so i can use it for both flyers and small posters

ADDITIONS

BIG BOLD HEADLINE TO GRAP ATTENTION, greatest prominence

sub headline to explain, smaller than the headline, but still prominent on the poster

just a few bullet points to list the benefits and answer the “whats in for me”-question
this is for people who are already interested and continue reading, medium prominence.

WHERE, WHEN, HOW MUCH-information, in the lower section of the poster, little text, but clearly visible

only one point of CONTACT on my poster “www.tobiaskernwald.com”, bit big and clear so that it is very prominent

little text, effectively used
LESS IS MORE
Updates

contact me regarding logo files and any questions you may have!

for the logo files go to

https://secure.dropvaultly.com/fs/v.aspx?v=41958b2d703c9ea1f6d2

click on the folder "logo pack" to see the files

eps
jpg
png
photoshop
TIF

thanks for your interest. hope to see great designs!
I am really looking forward to it
if you have any questions, please do not hesitate to ask

Kind Regards
Tobias
 

• Simple, clean design, text sparingly used.

• The mood should be light-hearted, calm, bright, simple and friendly, comic like

• a lot of white space, calling more attention to the content

• a light blue, dark blue, white and black colour scheme as seen on the homepage (www.tobiaskernwald.com) please use the exact same colours as seen on the homepage.

White being most predominant, 2 different blue used to highlight something, black for text on white background.

• One graphic would be cool, as long as it is blue. It could be waves-like graphic, or something like the white pattern in the background, in my case just in blue on white background > http://www.lumenquietharbor.org/., I do not mean exactly this graphic and not that crowded but a simple single graphic in blue as long as it fits the theme and feel of my poster

Top o f the poster

• (a )One short bold headline (TALK TITLE) with a sub-headline below it (hook)

• or (b) headline as question (…....?) and below sub-headline offering the solution (my talk ;-) of course)

• 3 benefits as on homepage, that I can adapt for each talk (bottom right of my start site “what are you looking for?” either blue on white, or as in the page white on blue...whatever looks better and fits the design). Not sure how that looks, and if to include it!

• the bottom of the poster will have “Where”-information “when”-information “ticket price” info

• contact at the very bottom...for more into or to purchase tickets (my website and email)

If you have any questions or need clarification please write me!

Requirements
Must have
• lot of white space
• less is more - simple design
• little text, little graphics- only used when necessary to greatest effect.
• light, friendly, modern feel
• blue-color scheme

```html
<!DOCTYPE html>
<html lang="en">
<head>
<meta charset="utf-8">
<title>Talk Poster – Tobias Kernwald</title>
<link rel="stylesheet" href="https://fonts.googleapis.com/css2?family=Arimo:ital,wght@0,400;0,700;1,400&display=swap">
<style>
  :root {
    --cyan: #5bc5e1;
    --cyan-light: #a9e0ef;
    --sky-wash: #e4f4fa;
    --navy: #3a6a8c;
    --slate: #6e8ea8;
    --grey: #8d9296;
    --grey-text: #8a8a8a;
    --ink: #1b1b1b;
    --rule: #dcdcdc;
    --band: #1aa3dc;
    --white: #ffffff;
  }
  * { margin: 0; padding: 0; box-sizing: border-box; }
  html, body { width: 856px; height: 1200px; overflow: hidden; background: var(--white); }
  body { font-family: "Arimo", Arial, sans-serif; position: relative; }

  .rule { position: absolute; left: 68px; width: 720px; height: 1px; background: var(--rule); }
  .rule--top { top: 213px; }
  .rule--mid { top: 770px; }

  .brand {
    position: absolute; top: 120px; right: 90px;
    display: flex; align-items: center; gap: 10px;
    font-weight: 700; font-size: 20px; color: var(--navy);
  }
  .brand__dot { width: 18px; height: 18px; border-radius: 50%; background: var(--cyan); }

  .hero { position: absolute; left: 68px; top: 230px; width: 721px; height: 515px; }
  .hero__shape { position: absolute; inset: 0; }
  .hero__title {
    position: absolute; left: 72px; top: 51px;
    font-weight: 700; font-size: 128px; letter-spacing: -6px; line-height: 1;
    color: var(--white); white-space: nowrap;
    text-shadow: 2px 3px 3px rgba(0,0,0,.28);
  }
  .hero__title .mark { color: var(--navy); }
  .hero__sub {
    position: absolute; left: 77px; top: 170px;
    font-weight: 700; font-size: 28px; line-height: 1; letter-spacing: -.5px; color: var(--ink);
    white-space: nowrap;
  }

  .benefits { position: absolute; left: 0; top: 312px; width: 721px; }
  .benefits__title {
    text-align: center; margin-left: 10px;
    font-weight: 700; font-size: 24px; letter-spacing: -.5px; color: var(--grey-text);
  }
  .benefits__title strong { color: var(--navy); }
  .benefits__rule {
    margin: 10px auto 0; width: 600px; height: 1px;
    background: linear-gradient(90deg, transparent, var(--white) 30%, var(--white) 70%, transparent);
    box-shadow: 0 -1px 0 rgba(0,0,0,.04);
  }
  .benefits__list { list-style: none; position: absolute; left: 259px; top: 48px; }
  .benefits__list li {
    display: flex; align-items: center; gap: 8px; height: 45px;
    font-style: italic; font-size: 17px; color: var(--grey-text);
  }
  .benefits__num {
    width: 25px; height: 25px; border-radius: 50%; background: var(--slate);
    color: var(--white); font-style: normal; font-weight: 700; font-size: 15px;
    display: flex; align-items: center; justify-content: center;
  }

  .info { position: absolute; top: 792px; width: 198px; height: 210px; }
  .info--where { left: 68px; }
  .info--when { left: 330px; }
  .info--tickets { left: 590px; }
  .info__shape { position: absolute; inset: 0; }
  .info__label {
    position: absolute; top: 20px; left: 41px; width: 115px; height: 29px;
    border-radius: 3px; color: var(--white); font-weight: 700; font-size: 16px;
    display: flex; align-items: center; justify-content: center;
  }
  .info--where .info__label { background: var(--navy); }
  .info--when .info__label { background: var(--cyan); }
  .info--tickets .info__label { background: var(--grey); }
  .info__rule { position: absolute; top: 62px; left: 20px; right: 20px; height: 1px; background: var(--white); }
  .info__text {
    position: absolute; top: 78px; left: 21px;
    font-size: 12px; line-height: 19px; color: var(--grey-text); letter-spacing: 0;
  }

  .contact { position: absolute; left: 68px; top: 1037px; width: 720px; height: 148px; }
  .contact__shape { position: absolute; inset: 0; border-radius: 26px 26px 0 0;
    background: linear-gradient(180deg, var(--sky-wash), #d4eef7); }
  .contact__dot { position: absolute; left: 50px; top: 48px; width: 30px; height: 30px; border-radius: 50%; background: var(--cyan); opacity: .8; }
  .contact__lead {
    position: absolute; top: 29px; left: 0; width: 734px; text-align: center;
    font-weight: 700; font-size: 16px; color: var(--grey-text);
  }
  .contact__rule { position: absolute; top: 55px; left: 118px; width: 545px; height: 1px; background: var(--white); }
  .contact__url {
    position: absolute; top: 66px; left: 0; width: 720px; text-align: center;
    font-weight: 700; font-size: 39px; letter-spacing: -1.5px; color: #4a4a4a;
  }
  .contact__url .accent { color: var(--cyan); }

  .band { position: absolute; left: 0; bottom: 0; width: 856px; height: 15px;
    background: linear-gradient(90deg, var(--band), #6fd0f0 50%, var(--band)); }
</style>
</head>
<body>
  <div class="rule rule--top"></div>

  <div class="brand"><span class="brand__dot"></span>Tobias Kernwald</div>

  <section class="hero">
    <svg class="hero__shape" width="721" height="515" viewBox="0 0 721 515" aria-hidden="true">
      <defs>
        <radialGradient id="heroBlue" cx="0.45" cy="0.65" r="0.7">
          <stop offset="0" stop-color="#c4ebf5"/>
          <stop offset="0.55" stop-color="#6fcbe4"/>
          <stop offset="1" stop-color="#58c2df"/>
        </radialGradient>
        <linearGradient id="heroWash" x1="0" y1="0" x2="0" y2="1">
          <stop offset="0" stop-color="#d6f0f8"/>
          <stop offset="1" stop-color="#ffffff"/>
        </linearGradient>
      </defs>
      <path d="M0 260 H721 V487 Q721 515 693 515 H28 Q0 515 0 487 Z" fill="url(#heroWash)"/>
      <path d="M28 0 H693 Q721 0 721 28 V232 Q721 260 693 260 H378 Q362 262 359 295 Q356 262 340 260 H28 Q0 260 0 232 V28 Q0 0 28 0 Z" fill="url(#heroBlue)"/>
    </svg>
    <h1 class="hero__title">Heading...<span class="mark">?</span></h1>
    <p class="hero__sub">Sub-Headline, ds sf sef ?</p>

    <div class="benefits">
      <h2 class="benefits__title">What’s <strong>in it for me?</strong></h2>
      <div class="benefits__rule"></div>
      <ol class="benefits__list">
        <li><span class="benefits__num">1</span>Improved self-esteem</li>
        <li><span class="benefits__num">2</span>Inner peace and calm</li>
        <li><span class="benefits__num">3</span>Greater purpose and meaning in life</li>
      </ol>
    </div>
  </section>

  <div class="rule rule--mid"></div>

  <svg width="0" height="0" style="position:absolute" aria-hidden="true">
    <defs>
      <linearGradient id="infoWash" x1="0" y1="0" x2="0" y2="1">
        <stop offset="0" stop-color="#e6f5fa"/>
        <stop offset="1" stop-color="#ffffff"/>
      </linearGradient>
    </defs>
  </svg>

  <article class="info info--where">
    <svg class="info__shape" width="198" height="210" viewBox="0 0 198 210" aria-hidden="true">
      <path d="M20 0 H178 Q198 0 198 20 V174 Q198 194 178 194 H112 Q102 196 99 206 Q96 196 86 194 H20 Q0 194 0 174 V20 Q0 0 20 0 Z" fill="url(#infoWash)"/>
    </svg>
    <h3 class="info__label">Where?</h3>
    <div class="info__rule"></div>
    <p class="info__text">??????????????????????<br>??????????????<br>????????????????????</p>
  </article>

  <article class="info info--when">
    <svg class="info__shape" width="198" height="210" viewBox="0 0 198 210" aria-hidden="true">
      <path d="M20 0 H178 Q198 0 198 20 V174 Q198 194 178 194 H112 Q102 196 99 206 Q96 196 86 194 H20 Q0 194 0 174 V20 Q0 0 20 0 Z" fill="url(#infoWash)"/>
    </svg>
    <h3 class="info__label">When?</h3>
    <div class="info__rule"></div>
    <p class="info__text">??????????????????????<br>??????????????<br>????????????????????</p>
  </article>

  <article class="info info--tickets">
    <svg class="info__shape" width="198" height="210" viewBox="0 0 198 210" aria-hidden="true">
      <path d="M20 0 H178 Q198 0 198 20 V174 Q198 194 178 194 H112 Q102 196 99 206 Q96 196 86 194 H20 Q0 194 0 174 V20 Q0 0 20 0 Z" fill="url(#infoWash)"/>
    </svg>
    <h3 class="info__label">Tickets?</h3>
    <div class="info__rule"></div>
    <p class="info__text">??????????????????????<br>??????????????<br>????????????????????</p>
  </article>

  <footer class="contact">
    <div class="contact__shape"></div>
    <span class="contact__dot"></span>
    <p class="contact__lead">For more information or to purchase tickets, visit:</p>
    <div class="contact__rule"></div>
    <p class="contact__url">www.<span class="accent">tobias</span>kernwald.co.uk</p>
  </footer>

  <div class="band"></div>
</body>
</html>
```